Flashy and colorful banner for an orange grower

Hi, I need a graphic for an advertising banner (80x200cm) to be placed next to the sales van. So far we have tried to highlight the naturalness of our products. With this banner we would like to highlight the ancient Sicilian tradition, with the typical decorations, I attach some photos as an example. We will sell our products far from Sicily, so I would like to exalt our origin.
We would like to dare with a colorful and amazing design, to capture the attention of passers-by.
It might be nice to insert or rework the decoration within our logo.
I would like to insert 4 of our offers inside the banner, only in the upper part, from the middle up.
The text is:
DAL CUORE DELLA SICILIA
ARANCIA TAROCCO
ALLA RINFUSA
5€ BORSA
DA SPREMERE
10€ CASSETTA
DA TAVOLA
15€ CASSETTA
SELEZIONE PREMIUM
20€ CASSETTA
Thanks for your time

```html
<!DOCTYPE html>
<html lang="it">
<head>
<meta charset="utf-8">
<title>Soleverde Sicilia – Roll-up</title>
<link rel="stylesheet" href="https://fonts.googleapis.com/css2?family=Gloock&family=Poppins:wght@500;600;700;800&display=swap">
<style>
  :root {
    --green: #1d6b34;
    --green-dark: #14522a;
    --orange: #e65a24;
    --orange-light: #f39a2b;
    --cream: #fbe0a0;
    --white: #ffffff;
  }
  * { margin: 0; padding: 0; box-sizing: border-box; }
  html, body { width: 1200px; height: 2679px; overflow: hidden; background: var(--white); }
  .banner { position: relative; width: 1200px; height: 2679px; background: var(--white); overflow: hidden; font-family: "Poppins", sans-serif; }

  .border-band { position: absolute; }
  .border-top { left: 0; top: 0; width: 1200px; height: 120px;
    background: linear-gradient(90deg, var(--green) 0 12%, var(--orange) 12% 14%, var(--cream) 14% 86%, var(--orange) 86% 88%, var(--green) 88% 100%); }
  .border-top::after { content: ""; position: absolute; left: 0; right: 0; top: 0; height: 60px;
    background: repeating-linear-gradient(90deg, var(--green) 0 18px, var(--orange) 18px 34px, var(--orange-light) 34px 46px, var(--white) 46px 60px); opacity: .85; }
  .border-left, .border-right { top: 120px; width: 110px; height: 2559px;
    background: repeating-linear-gradient(180deg, var(--green) 0 30px, var(--orange) 30px 52px, var(--orange-light) 52px 68px, var(--white) 68px 84px); }
  .border-left { left: 0; }
  .border-right { right: 0; }
  .border-left::after, .border-right::after { content: ""; position: absolute; top: 0; bottom: 0; width: 28px; background: var(--white); }
  .border-left::after { right: 0; }
  .border-right::after { left: 0; }

  .brand { position: absolute; left: 0; width: 1200px; top: 400px;
    display: flex; align-items: center; justify-content: center; gap: 24px; }
  .brand-dot { width: 56px; height: 56px; border-radius: 50%; background: var(--orange-light); flex: none; }
  .brand-name { font-size: 66px; font-weight: 600; line-height: 1; color: var(--green); letter-spacing: 1px; }

  .offer { position: absolute; width: 445px; height: 445px; border-radius: 50%;
    background: radial-gradient(circle, var(--cream) 62%, var(--orange-light) 63% 66%, var(--cream) 67% 88%, var(--orange) 89% 100%); }
  .offer-ring { position: absolute; inset: 0; border-radius: 50%;
    background: repeating-conic-gradient(var(--green) 0 4deg, transparent 4deg 12deg, var(--orange) 12deg 15deg, transparent 15deg 24deg);
    -webkit-mask: radial-gradient(circle, transparent 66%, #000 67% 87%, transparent 88%);
            mask: radial-gradient(circle, transparent 66%, #000 67% 87%, transparent 88%); opacity: .55; }
  .offer-core { position: absolute; left: 77px; top: 77px; width: 291px; height: 291px; border-radius: 50%;
    display: flex; flex-direction: column; align-items: center; justify-content: center; text-align: center; }
  .offer-core--orange { background: var(--orange); }
  .offer-core--green { background: var(--green); }
  .offer-title { font-size: 36px; font-weight: 700; line-height: 1.1; color: var(--white); }
  .offer-price { font-size: 96px; font-weight: 800; line-height: 1; color: var(--cream); margin-top: 4px; }
  .offer-price sup { font-size: 48px; vertical-align: 38px; }
  .offer-unit { font-size: 22px; font-weight: 500; letter-spacing: 7px; color: var(--white); margin-top: 8px; }

  .offer-1 { left: 136px; top: 636px; }
  .offer-2 { left: 620px; top: 636px; }
  .offer-3 { left: 136px; top: 1074px; }
  .offer-4 { left: 620px; top: 1074px; }

  .headline { position: absolute; left: 0; width: 1200px; top: 1548px; text-align: center;
    font-family: "Gloock", serif; font-size: 98px; line-height: 0.92; letter-spacing: 2px; font-weight: 400; }
  .headline-line { display: block; }
  .headline-line--green { color: var(--green); }
  .headline-line--orange { color: var(--orange); }

  .fruit-art { position: absolute; left: -10px; top: 1950px; width: 1220px; height: 1220px; border-radius: 50%;
    background: radial-gradient(circle at 50% 50%, var(--orange) 0 40%, var(--orange-light) 41% 46%, var(--cream) 47% 58%, var(--orange-light) 59% 64%, var(--orange) 65% 100%); }

  .web-band { position: absolute; left: 0; top: 2508px; width: 1200px; height: 105px; background: var(--green);
    display: flex; align-items: center; justify-content: center;
    font-size: 50px; font-weight: 600; color: var(--white); letter-spacing: 2px; }
</style>
</head>
<body>
<main class="banner">
  <div class="border-band border-top" role="img" aria-label="Fascia decorativa siciliana con foglie verdi e motivi arancio"></div>
  <div class="border-band border-left" role="img" aria-label="Cornice decorativa siciliana a volute verdi e arancio"></div>
  <div class="border-band border-right" role="img" aria-label="Cornice decorativa siciliana a volute verdi e arancio"></div>

  <header class="brand">
    <span class="brand-dot"></span>
    <p class="brand-name">SOLEVERDE SICILIA</p>
  </header>

  <section class="offers">
    <div class="offer offer-1">
      <div class="offer-ring" role="img" aria-label="Cornice circolare decorata in stile carretto siciliano"></div>
      <div class="offer-core offer-core--orange">
        <p class="offer-title">ALLA<br>RINFUSA</p>
        <p class="offer-price">5<sup>€</sup></p>
        <p class="offer-unit">BORSA</p>
      </div>
    </div>
    <div class="offer offer-2">
      <div class="offer-ring" role="img" aria-label="Cornice circolare decorata in stile carretto siciliano"></div>
      <div class="offer-core offer-core--green">
        <p class="offer-title">DA<br>SPREMERE</p>
        <p class="offer-price">10<sup>€</sup></p>
        <p class="offer-unit">CASSETTA</p>
      </div>
    </div>
    <div class="offer offer-3">
      <div class="offer-ring" role="img" aria-label="Cornice circolare decorata in stile carretto siciliano"></div>
      <div class="offer-core offer-core--green">
        <p class="offer-title">DA<br>TAVOLA</p>
        <p class="offer-price">15<sup>€</sup></p>
        <p class="offer-unit">CASSETTA</p>
      </div>
    </div>
    <div class="offer offer-4">
      <div class="offer-ring" role="img" aria-label="Cornice circolare decorata in stile carretto siciliano"></div>
      <div class="offer-core offer-core--orange">
        <p class="offer-title">SELEZIONE<br>PREMIUM</p>
        <p class="offer-price">20<sup>€</sup></p>
        <p class="offer-unit">CASSETTA</p>
      </div>
    </div>
  </section>

  <h1 class="headline">
    <span class="headline-line headline-line--green">DAL CUORE</span>
    <span class="headline-line headline-line--orange">DELLA SICILIA</span>
    <span class="headline-line headline-line--green">ARANCI TAROCCO</span>
  </h1>

  <div class="fruit-art" role="img" aria-label="Illustrazione di una grande fetta d'arancia decorata con motivi floreali siciliani"></div>

  <footer class="web-band">www.soleverdesicilia.com</footer>
</main>
</body>
</html>
```